Lumo Tavi Menu Design Project

This project is pretty straight forward. You will be given 3 files which include the following:
1. Our proposed menu
2. Our Company logo
3. A sample menu on what we are looking for design wise

Your job is to create a visually pleasing menu that is simple, clean and fresh. Please refer to our home website for additional information. (www.lumotavi.example) Must be in eps or equivalent format.

Target Market(s)

20s to 40s

Industry/Entity Type

It Company

Requirements
Must have
• Company log
Must be in EPS format

```html
<!DOCTYPE html>
<html lang="en">
<head>
<meta charset="utf-8">
<title>Lumo Tavi Menu</title>
<link href="https://fonts.googleapis.com/css2?family=Oswald:wght@300&family=Roboto+Condensed:wght@500&family=Playfair+Display:ital@1&family=Merriweather:wght@700&family=Open+Sans&display=swap" rel="stylesheet">
<style>
:root{
  --backdrop:#ece4d6;
  --paper:#ffffff;
  --orange:#f26a1f;
  --orange-light:#f7a36d;
  --red:#c0282d;
  --rust:#c0561e;
  --ink:#1d1d1d;
  --muted:#6d6d6d;
  --band:#e6dccb;
  --steel:#9aa0a5;
}
*{margin:0;padding:0;box-sizing:border-box}
html,body{width:1200px;height:746px;overflow:hidden;background:var(--backdrop)}
.stage{position:relative;width:1200px;height:746px}
.panel{position:absolute;top:25px;height:685px;background:var(--paper);overflow:hidden}
.panel--cover{left:38px;width:417px}
.panel--index{left:482px;width:208px}
.panel--dimsum{left:716px;width:206px}
.panel--salad{left:945px;width:210px}
.photo{position:absolute}
.brand{position:absolute;border-radius:50%;background:#fff;box-shadow:0 2px 5px rgba(0,0,0,.25);display:flex;align-items:center;justify-content:center;font-family:"Roboto Condensed",sans-serif;font-weight:500;color:var(--red);text-align:center;line-height:1}
/* cover */
.cover-interior{left:0;top:0;width:417px;height:197px;background:linear-gradient(180deg,#3a2716 0%,#5c3a1f 45%,#2b1a10 100%)}
.cover-body{position:absolute;left:0;top:197px;width:417px;height:488px;background:radial-gradient(ellipse at 40% 30%,#f4f4f4 0%,#cfd2d4 55%,#8f9599 100%)}
.cover-dish{left:150px;top:395px;width:267px;height:290px;background:linear-gradient(160deg,#f7f7f7 0%,#e8e8e8 35%,#4a5a2e 55%,#3a2418 100%);border-top-left-radius:60px}
.cover .brand{left:152px;top:135px;width:100px;height:100px;font-size:17px}
.tagline{position:absolute;left:0;width:417px;text-align:center;font-family:"Playfair Display",serif;font-style:italic}
.tagline--lead{top:308px;font-size:20px;color:var(--ink)}
.tagline--main{top:340px;font-size:33px;letter-spacing:3px;color:var(--rust)}
/* index */
.index-head{position:absolute;left:0;top:0;width:208px;height:132px;background:linear-gradient(180deg,#f15a1c,#f68a3c)}
.index-head .brand{left:66px;top:12px;width:76px;height:76px;font-size:13px}
.index-word{position:absolute;left:0;top:82px;width:208px;text-align:center;font-family:"Oswald",sans-serif;font-weight:300;font-size:50px;color:var(--orange-light);line-height:1;letter-spacing:1px}
.index-list{position:absolute;left:0;top:172px;width:208px;list-style:none}
.index-list li{position:relative;height:39.2px;display:flex;align-items:center}
.index-list span{padding-left:14px;font-family:"Roboto Condensed",sans-serif;font-weight:500;font-size:13px;color:var(--ink)}
.index-list i{position:absolute;left:84px;top:2px;width:115px;height:34px;background:linear-gradient(90deg,rgba(255,255,255,0),#c98b4a 30%,#8a4a22)}
.foot{position:absolute;left:0;bottom:0;width:100%;height:20px;background:var(--band)}
.foot b{position:absolute;left:0;top:0;width:16px;height:20px;background:var(--orange);color:#fff;font:11px "Open Sans",sans-serif;display:flex;align-items:center;justify-content:center}
/* menu pages */
.page-head{left:84px;top:15px;width:122px;height:36px;background:linear-gradient(90deg,rgba(255,255,255,0),#e9dcbc 30%,#c7b58e)}
.page .brand{left:30px;top:13px;width:40px;height:40px;font-size:8px}
.section{position:absolute;left:32px;font-family:"Oswald",sans-serif;font-weight:300;font-size:22px;color:var(--ink);line-height:1;text-transform:uppercase}
.items{position:absolute;left:32px;width:150px;list-style:none}
.items li{margin-bottom:14px}
.items h3{font-family:"Merriweather",serif;font-size:5.6px;color:var(--red);font-weight:700;line-height:1.2}
.items h3::after{content:"";display:inline-block;width:6px;height:4px;margin-left:4px;background:#c6b34a;vertical-align:middle}
.items p{font-family:"Open Sans",sans-serif;font-size:4.6px;color:var(--muted);line-height:1.35;margin-top:1px}
.hot{display:inline-block;width:4px;height:4px;border-radius:50%;background:var(--red);margin-right:3px;vertical-align:middle}
.section-photo{height:35px;background:linear-gradient(90deg,rgba(255,255,255,0),#d6a35c 30%,#8d3a1c)}
.note{position:absolute;left:32px;top:602px;width:170px;font-family:"Open Sans",sans-serif;font-weight:700;font-size:4.8px;color:var(--red);line-height:1.4}
</style>
</head>
<body>
<main class="stage">

  <section class="panel panel--cover cover">
    <div class="photo cover-interior" role="img" aria-label="Photo of the restaurant dining room with booths and warm lights"></div>
    <div class="cover-body"></div>
    <div class="photo cover-dish" role="img" aria-label="Photo of beef with green beans on a white plate"></div>
    <div class="brand">Lumo Tavi</div>
    <p class="tagline tagline--lead">Experience the Art of</p>
    <p class="tagline tagline--main">Chinese Cuisine</p>
  </section>

  <section class="panel panel--index">
    <div class="index-head">
      <div class="brand">Lumo Tavi</div>
      <p class="index-word">menu</p>
    </div>
    <ul class="index-list">
      <li><span>Dim Sum</span><i role="img" aria-label="Photo of dumplings"></i></li>
      <li><span>Salads</span><i role="img" aria-label="Photo of a salad"></i></li>
      <li><span>Soup</span><i role="img" aria-label="Photo of soup"></i></li>
      <li><span>Chicken</span><i role="img" aria-label="Photo of a chicken dish"></i></li>
      <li><span>Beef / Pork</span><i role="img" aria-label="Photo of a pork dish"></i></li>
      <li><span>Combination</span><i role="img" aria-label="Photo of a combination plate"></i></li>
      <li><span>Seafood</span><i role="img" aria-label="Photo of shrimp"></i></li>
      <li><span>Vegetables</span><i role="img" aria-label="Photo of vegetables"></i></li>
      <li><span>Rice &amp; Mushu</span><i role="img" aria-label="Photo of fried rice"></i></li>
      <li><span>Noodles</span><i role="img" aria-label="Photo of noodles"></i></li>
      <li><span>Desserts</span><i role="img" aria-label="Photo of a chocolate dessert"></i></li>
      <li><span>Beverages</span><i role="img" aria-label="Photo of a drink"></i></li>
    </ul>
    <div class="foot"><b>1</b></div>
  </section>

  <section class="panel panel--dimsum page">
    <div class="photo page-head" role="img" aria-label="Photo of steamed dumplings"></div>
    <div class="brand">Lumo Tavi</div>
    <h2 class="section" style="top:72px">Dim Sum</h2>
    <ul class="items" style="top:104px">
      <li><h3>Steamed Dumplings $6.50</h3><p>Five steamed dumplings with chicken, pork or vegetable.</p></li>
      <li><h3>Won Ton Skin $7.25</h3><p>Crisp wonton skins filled with cream cheese, crab.</p></li>
      <li><h3><span class="hot"></span>Szechuan Dumplings $6.25</h3><p>Pork dumplings tossed in a spicy chili sauce.</p></li>
      <li><h3>Bao $5.95</h3><p>Three fluffy steamed buns filled with barbecued pork.</p></li>
      <li><h3>Vietnamese Summer Rolls $4.95</h3><p>Rice paper rolls with lettuce, herbs and noodles.</p></li>
      <li><h3>Pan-Fried Potstickers $6.50</h3><p>Pan fried dumplings with chicken, pork or vegetable.</p></li>
      <li><h3>Gift Wrapped Chicken $5.95</h3><p>Six chicken tenders marinated in soy, sesame, garlic.</p></li>
      <li><h3>Fried Won Tons $5.95</h3><p>Crispy wontons with chicken or pork, apricot sauce.</p></li>
      <li><h3>Pot Stew $6.95</h3><p>Pan seared crescents with shrimp and bamboo shoots.</p></li>
      <li><h3>Vietnamese Shrimp Summer Rolls $5.95</h3><p>Two rice paper rolls with shrimp and mint.</p></li>
      <li><h3>Shu Mai $5.95</h3><p>Six steamed open dumplings with pork and shrimp.</p></li>
      <li><h3>Spring Rolls $4.50</h3><p>Two spring rolls with chicken or vegetable filling.</p></li>
      <li><h3>Cantonese Dumplings $5.95</h3><p>Four crispy dumplings filled with chicken and shrimp.</p></li>
      <li><h3>Shrimp Toast $5.95</h3><p>Toasted bread topped with shrimp, water chestnut, scallion.</p></li>
      <li><h3>Assorted Pleasures $8.95</h3><p>A combination of potstickers, wontons, chicken and rolls.</p></li>
    </ul>
    <div class="foot"><b>2</b></div>
  </section>

  <section class="panel panel--salad page">
    <div class="photo page-head" role="img" aria-label="Photo of a Chinese chicken salad"></div>
    <div class="brand">Lumo Tavi</div>
    <h2 class="section" style="top:72px">Salad</h2>
    <ul class="items" style="top:104px">
      <li><h3>Chinese Chicken Salad $10.50</h3><p>Shredded lettuce, chicken, carrots, almonds and crisp noodles.</p></li>
      <li><h3>Sesame Chicken Salad $9.95</h3><p>Greens, sliced chicken, mandarin oranges, sesame ginger dressing.</p></li>
      <li><h3><span class="hot"></span>Mein Mein Salad $9.75</h3><p>Cold lo mein noodles with chicken, vegetables, peanuts.</p></li>
      <li><h3>Asian Pear Salad $9.50</h3><p>Mixed greens, pears, walnuts and bleu cheese crumbles.</p></li>
      <li><h3>Jade Salad $11.25</h3><p>Spinach, shrimp, scallops and oranges with citrus vinaigrette.</p></li>
    </ul>
    <h2 class="section" style="top:260px">Soup</h2>
    <div class="photo section-photo" style="left:95px;top:253px;width:115px" role="img" aria-label="Photo of a soup bowl"></div>
    <ul class="items" style="top:298px">
      <li><h3><span class="hot"></span>Hot and Sour Soup (S) $4.95 / (L) $7.50</h3><p>Shredded pork, mushrooms, bamboo, egg and silken tofu.</p></li>
      <li><h3>Velvet Corn Soup $7.25</h3><p>Creamy corn soup with chicken, green peas, egg.</p></li>
      <li><h3>Won Ton Soup (S) $4.95 / (L) $7.50</h3><p>Pork and shrimp wontons with spinach in broth.</p></li>
      <li><h3>Wor Won Ton Soup $9.95</h3><p>Wontons with shrimp, chicken, pork and fresh vegetables.</p></li>
      <li><h3>House Noodle Soup (S) $4.95 / (L) $7.50</h3><p>Chicken and barbecued pork with noodles in broth.</p></li>
    </ul>
    <h2 class="section" style="top:440px">Chicken</h2>
    <div class="photo section-photo" style="left:85px;top:430px;width:125px" role="img" aria-label="Photo of a glazed chicken dish"></div>
    <ul class="items" style="top:470px">
      <li><h3>Tangerine Chicken $11.75</h3><p>Crispy chicken tossed with scallions in tangerine sauce.</p></li>
      <li><h3><span class="hot"></span>Kung Pao Chicken $12.95</h3><p>Dark meat chicken with peanuts and chili peppers.</p></li>
      <li><h3>Moo Goo Gai Pan $11.95</h3><p>Chicken breast with mushrooms, snow peas, water chestnuts.</p></li>
      <li><h3>Lemon Chicken $11.75</h3><p>Crispy chicken breast in a tangy lemon glaze.</p></li>
      <li><h3>House Chicken $11.95</h3><p>Wok fried chicken with garlic, ginger and scallion.</p></li>
    </ul>
    <p class="note">All White Meat Chicken $1.00 Extra.<br>Enjoy a Half Chinese Chicken Salad or Plain Fried Rice with any entree for $5.50.</p>
    <div class="foot"><b>3</b></div>
  </section>

</main>
</body>
</html>
```